International freight forwarder experienced in perishable handling needs a web design

We need a website designed that will allow us to capture more customers through the website. We would like a visually appealing design that is not so heavy on text. Our business covers the logistics and freight forwarding industries and we have offices in South America and the USA. Our main customers are importers USA, Europe, Asia and Russia and we currently work almost exclusively with perishable products such as fresh cut flowers, fresh exotics fruits, cacao, fresh fish etc. We would like to convey a fresh, modern approach to freight forwarding focusing on concepts such as - time sensitive, anytime-anywhere delivery, innovation, experience, reliability and confidence. Should include links with Plumetta and Worvanet. Our core solutions include: Core Services
*Air Freight
*Ocean Freight
*Warehousing & Distribution
Our industry solutions cover
*Flowers
*FMCG including, fruits, vegetables
*Live animals
*Automotive
*Consumer Goods
*Industrial
*Oil & Gas
*Pharma
* Event logistics
* Project logistics

Target Market(s)

Importers in Europe, USA, Asia, Middle East and Russia

Number of Pages Required

4 page

Font styles to use
Sans Serif

Colors
a1cd39
606060
000000

Requirements
Must have
• Photos of fresh cut flowers, FMCG such as cacao, fresh fish (packaged for shipping), fresh exotic fruits, pharma products (packaged for shipping), oil and gas etc. Internal customer login access
Nice to have
• Photos of cargo shipping carriers and cargo airline carriers. Features similar to those of following website http://www.brolvacargo.com/eng/main/index.jsp?FromURL=web
Should not have
• Too much text, needs to be visually pleasing

```html
<!DOCTYPE html>
<html lang="en">
<head>
<meta charset="utf-8">
<title>Vantrel Freight Group</title>
<link href="https://fonts.googleapis.com/css2?family=Arimo:wght@400;700&family=Open+Sans:wght@400;600&display=swap" rel="stylesheet">
<style>
:root{
  --green:#7cb22a;
  --green-dark:#5f9417;
  --green-light:#a1cd39;
  --grey:#606060;
  --text:#333;
  --body:#555;
  --panel:#f3f3f3;
  --footer:#4a4a4a;
  --link:#1a5fb4;
}
*{box-sizing:border-box;margin:0;padding:0}
html,body{width:900px;height:1200px;overflow:hidden;background:#fff}
body{position:relative;font-family:"Arimo",Arial,sans-serif;color:var(--text)}
.abs{position:absolute}
.top-rule{left:0;top:0;width:900px;height:4px;background:var(--green)}
.brand{left:97px;top:14px;display:flex;align-items:center;gap:10px}
.brand-mark{width:52px;height:52px;background:var(--green)}
.brand-name{font-size:30px;font-weight:700;color:var(--grey);line-height:1.1}
.brand-name small{display:block;font-size:17px;letter-spacing:6px;font-weight:700;color:var(--grey)}
.call{right:95px;top:22px;text-align:left}
.call-label{font-size:14px;color:var(--green)}
.call-number{font-size:22px;color:var(--grey);letter-spacing:.5px}
.login{right:95px;top:66px;font-size:11px;font-weight:700;color:var(--green);display:flex;align-items:center;gap:5px}
.nav{left:0;top:86px;width:900px;height:34px;background:linear-gradient(#8cc43a,#6aa51f);border-top:2px solid var(--green-dark);border-bottom:2px solid var(--green-dark)}
.nav ul{list-style:none;display:flex;margin-left:103px;height:100%}
.nav li{color:#fff;font-size:12.5px;padding:0 14px;display:flex;align-items:center;border-right:1px solid rgba(255,255,255,.35)}
.nav li:last-child{border-right:0}
.stage{left:0;top:120px;width:900px;height:305px;background:linear-gradient(90deg,#fafafa,#eee,#fafafa)}
.hero{left:99px;top:126px;width:702px;height:297px;border:3px solid #e4e4e4;background:linear-gradient(160deg,#dfe9d2 0%,#c7d9b0 35%,#e7a86a 65%,#b5574a 100%)}
.hero-band{left:0;top:108px;width:430px;height:72px;background:rgba(124,178,42,.78)}
.hero-title{left:22px;top:120px;width:330px;font-size:19px;line-height:24px;color:#fff}
.btn{background:linear-gradient(#7fb52e,#5d9418);color:#fff;font-size:12px;display:flex;align-items:center;justify-content:center;border-radius:2px;white-space:nowrap}
.hero-btn{left:22px;top:186px;width:139px;height:33px}
.dots{left:22px;top:257px;display:flex;gap:3px}
.dots span{width:13px;height:13px;border-radius:50%;background:#fff}
.dots span:first-child{background:var(--green-light)}
.service{top:444px;width:225px;height:112px;background:var(--panel);border-left:4px solid var(--green);border-bottom:4px solid var(--green)}
.service .thumb{left:10px;top:14px;width:86px;height:85px}
.service h3{left:118px;top:40px;font-size:15px;font-weight:400;color:var(--green);line-height:18px}
.rule{left:97px;width:706px;height:1px;background:#e2e2e2}
.h2{font-size:16px;font-weight:400;color:#222}
.h2 em{font-style:normal;color:var(--green)}
.para{font-family:"Open Sans",sans-serif;font-size:10.2px;line-height:18px;color:var(--body)}
.welcome-text{left:97px;top:637px;width:390px}
.read-more{left:97px;top:768px;width:95px;height:27px}
.network{left:518px;top:613px;width:285px;height:179px;background:var(--panel)}
.network .h2{left:17px;top:15px}
.network .para{left:17px;top:40px;width:118px}
.network .map{left:140px;top:40px;width:135px;height:100px}
.net-btn{left:15px;top:140px;width:134px;height:24px}
.news-item{left:97px;width:333px;height:70px}
.news-item .thumb{left:0;top:0;width:76px;height:70px}
.news-item h4{left:92px;top:-2px;width:245px;font-size:12.3px;font-weight:400;line-height:15px;color:var(--link)}
.news-item .para{left:92px;top:32px;width:245px;font-size:9.9px;line-height:15px}
.video{left:458px;top:879px;width:165px;height:104px}
.play{left:63px;top:33px}
.video-text{left:637px;top:875px;width:170px;font-size:12.2px;line-height:15px;color:#444}
.watch-btn{left:636px;top:940px;width:120px;height:25px}
.quote{left:457px;top:995px;width:348px;height:55px;font-size:15px;font-weight:700;letter-spacing:.3px;border-radius:3px}
.footer{left:0;top:1074px;width:900px;height:126px;background:var(--footer)}
.foot-nav{left:98px;top:24px;font-family:"Open Sans",sans-serif;font-size:9.2px;color:#eee;letter-spacing:.2px}
.follow{left:669px;top:22px;font-family:"Open Sans",sans-serif;font-size:9.5px;font-weight:600;color:#fff}
.socials{left:670px;top:46px;display:flex;gap:6px}
.socials span{width:22px;height:22px;border-radius:3px}
.copy{left:98px;top:73px;font-family:"Open Sans",sans-serif;font-size:8.5px;color:#fff;line-height:14px}
.copy small{display:block;color:#999;font-size:8.5px}
</style>
</head>
<body>
<div class="abs top-rule"></div>

<header>
  <div class="abs brand">
    <span class="brand-mark" aria-hidden="true"></span>
    <div class="brand-name">Vantrel Freight<small>GROUP</small></div>
  </div>
  <div class="abs call">
    <div class="call-label">Call US:</div>
    <div class="call-number">121 000 4870</div>
  </div>
  <div class="abs login">
    <svg width="10" height="11" viewBox="0 0 10 11" aria-hidden="true"><rect x="1" y="5" width="8" height="6" rx="1" fill="#7cb22a"/><path d="M3 5V3.5a2 2 0 0 1 4 0V5" fill="none" stroke="#7cb22a" stroke-width="1.4"/></svg>
    CUSTOMER LOGIN
  </div>
</header>

<nav class="abs nav">
  <ul>
    <li>HOME</li><li>ABOUT US</li><li>OUR SERVICES</li><li>RATES</li><li>LOCATION</li><li>CONTACT US</li>
  </ul>
</nav>

<div class="abs stage"></div>
<section class="abs hero">
  <div class="abs" role="img" aria-label="Photo of fresh cut flowers and exotic fruits packed in cold-chain cartons beside a cargo plane" style="inset:0"></div>
  <div class="abs hero-band"></div>
  <p class="abs hero-title">Fresh perishables, delivered anytime, anywhere...</p>
  <div class="abs btn hero-btn">Request a Quote</div>
  <div class="abs dots"><span></span><span></span><span></span></div>
</section>

<section>
  <div class="abs service" style="left:97px">
    <div class="abs thumb" role="img" aria-label="Photo of cargo aircraft being loaded with chilled pallets" style="background:linear-gradient(#b9cfe3,#7d8c99)"></div>
    <h3 class="abs">AIR<br>FREIGHT</h3>
  </div>
  <div class="abs service" style="left:337px">
    <div class="abs thumb" role="img" aria-label="Photo of a reefer container ship at sea" style="background:linear-gradient(#a9c4dc,#6f7f8f 55%,#2c4f7a)"></div>
    <h3 class="abs">OCEAN<br>FREIGHT</h3>
  </div>
  <div class="abs service" style="left:577px">
    <div class="abs thumb" role="img" aria-label="Photo of packed fresh fish and cut flowers in cold storage" style="background:linear-gradient(#d7e6ee,#9bb6c4 55%,#c9566a)"></div>
    <h3 class="abs">PERISHABLE<br>CARGO</h3>
  </div>
</section>

<div class="abs rule" style="top:585px"></div>

<section>
  <h2 class="abs h2" style="left:97px;top:610px">Welcome TO <em>Vantrel Freight Group</em></h2>
  <p class="abs para welcome-text">We move time-sensitive cargo from South America and the USA to importers in Europe, Asia, Russia and the Middle East. Fresh cut flowers, exotic fruits, cacao and fresh fish travel in a controlled cold chain from farm to final door. Our offices handle air freight, ocean freight, warehousing and distribution, with teams who know perishables. Pharma, oil and gas, automotive and event cargo receive the same care. Years of experience give our clients reliability and confidence in every single shipment we handle.</p>
  <div class="abs btn read-more">Read More</div>
</section>

<aside class="abs network">
  <h2 class="abs h2">OUR <em>NETWORK</em></h2>
  <p class="abs para">Offices in South America and the USA, serving importers on every continent.</p>
  <div class="abs map" role="img" aria-label="Dark world map with orange shipping routes" style="background:radial-gradient(ellipse at center,#3a3a3a 0%,#6a6a6a 55%,rgba(243,243,243,0) 72%)"></div>
  <div class="abs btn net-btn">SEE OUR LOCATION</div>
</aside>

<div class="abs rule" style="top:826px"></div>

<section>
  <h2 class="abs h2" style="left:98px;top:846px">LATEST <em>NEWS</em></h2>
  <article class="abs news-item" style="top:880px">
    <div class="abs thumb" role="img" aria-label="Photo of boxed roses ready for export" style="background:linear-gradient(#e6a0a8,#a85a64)"></div>
    <h4 class="abs">Valentine's flower season: extra charter capacity to Europe..</h4>
    <p class="abs para">More weekly flights for fresh cut flowers, with cold rooms at origin and fast customs clearance at arrival....</p>
  </article>
  <div class="abs" style="left:97px;top:961px;width:333px;height:1px;background:#e2e2e2"></div>
  <article class="abs news-item" style="top:977px">
    <div class="abs thumb" role="img" aria-label="Photo of a container ship at sea" style="background:linear-gradient(#bcd3e8,#6f7f8f 55%,#2c4f7a)"></div>
    <h4 class="abs">New reefer ocean service for exotic fruits and cacao..</h4>
    <p class="abs para">A weekly temperature-controlled sailing now links our South American ports with importers in Asia....</p>
  </article>
</section>

<section>
  <h2 class="abs h2" style="left:458px;top:846px">WATCH <em>HOW WE WORK</em></h2>
  <div class="abs video" role="img" aria-label="Video still of a cold storage warehouse aisle" style="background:linear-gradient(#8d9aa2,#b8c4ca 60%,#9aa2a4)">
    <svg class="abs play" width="40" height="40" viewBox="0 0 40 40" aria-hidden="true">
      <circle cx="20" cy="20" r="18" fill="rgba(0,0,0,.25)" stroke="#fff" stroke-width="2.5"/>
      <path d="M15 11 L29 20 L15 29 Z" fill="#fff"/>
    </svg>
  </div>
  <p class="abs video-text">From harvest to your door, see our cold chain at work..</p>
  <div class="abs btn watch-btn">Watch Full Video</div>
  <div class="abs btn quote">REQUEST A FREE QUOTE NOW !</div>
</section>

<footer class="abs footer">
  <p class="abs foot-nav">HOME &nbsp;/&nbsp; ABOUT US &nbsp;/&nbsp; OUR SERVICES &nbsp;/&nbsp; TRANSPORTATION &nbsp;/&nbsp; LOGISTICS &nbsp;/&nbsp; LATEST NEWS &nbsp;/&nbsp; CONTACT US</p>
  <p class="abs follow">FOLLOW US ON:</p>
  <div class="abs socials">
    <span style="background:#3b5998" aria-label="Plumetta"></span>
    <span style="background:#3fa9d8" aria-label="Social link"></span>
    <span style="background:#1f73b0" aria-label="Worvanet"></span>
    <span style="background:#f28a1e" aria-label="News feed"></span>
    <span style="background:#d22b2b" aria-label="Video channel"></span>
  </div>
  <p class="abs copy">© 2015 Vantrel Freight Group.<small>All Right Reserved</small></p>
</footer>
</body>
</html>
```